Private Medical Clinic needs a letterhead design

Letterhead that can be edited. Letter head is needed for printing official doctor's notes, referrals, etc in a medical clinic. The letterhead should use the attached logos

```html
<!DOCTYPE html>
<html lang="en">
<head>
<meta charset="utf-8">
<title>Willow Creek Family Medicine – Letterhead</title>
<link rel="stylesheet" href="https://fonts.googleapis.com/css2?family=EB+Garamond:wght@400&family=PT+Sans:wght@400;700&display=swap">
<style>
  :root {
    --backdrop: #ebeced;
    --paper: #ffffff;
    --brand-green: #4a5e3e;
    --band-green: #445a39;
    --gold-light: #f3df86;
    --gold-deep: #c9982f;
    --ink: #1e1e1e;
    --watermark: #eeefef;
    --white: #ffffff;
  }
  * { box-sizing: border-box; margin: 0; padding: 0; }
  html, body {
    width: 895px; height: 1200px; overflow: hidden;
    background: var(--backdrop);
  }
  .letterhead {
    position: absolute; left: 78px; top: 77px;
    width: 740px; height: 1045px;
    background: var(--paper);
    box-shadow: 0 0 14px rgba(0,0,0,0.08);
    overflow: hidden;
  }
  .brand {
    position: absolute; left: 32px; top: 74px;
    font-family: "EB Garamond", Georgia, serif;
    font-weight: 400; color: var(--brand-green);
  }
  .brand-name { font-size: 52px; line-height: 1; letter-spacing: -0.5px; }
  .brand-sub { font-size: 13.5px; letter-spacing: 2px; margin-top: 6px; margin-left: 2px; }
  .masthead-right {
    position: absolute; left: 432px; top: 106px; width 264px;
    width: 264px; text-align: center;
    font-family: "PT Sans", Arial, sans-serif; color: var(--brand-green);
  }
  .tagline {
    font-size: 19px; letter-spacing: 0.1px; line-height: 1;
    padding-bottom: 4px; border-bottom: 1px solid var(--brand-green);
  }
  .doctor { font-size: 17.5px; font-weight: 700; margin-top: 13px; }
  .rx {
    position: absolute; left: 102px; top: 264px;
    font-family: "EB Garamond", Georgia, serif; color: var(--ink);
    font-size: 28px; line-height: 1;
  }
  .rx sub { font-size: 24px; margin-left: -6px; vertical-align: -8px; }
  .watermark-area {
    position: absolute; left: 190px; top: 390px;
    width: 360px; height: 450px; border-radius: 50%;
    background: radial-gradient(ellipse at center, var(--watermark) 0%, rgba(238,239,239,0) 70%);
  }
  .footer { position: absolute; left: 0; bottom: 0; width: 740px; height: 80px; }
  .footer svg { position: absolute; left: 0; top: 0; }
  .footer-text {
    position: absolute; left: 0; width: 100%;
    font-family: "PT Sans", Arial, sans-serif; font-size: 12.5px;
    color: var(--white); display: flex; justify-content: center; align-items: center; gap: 14px;
  }
  .address { top: 35px; }
  .contacts { top: 58px; }
  .item { display: flex; align-items: center; gap: 5px; white-space: nowrap; }
  .item svg { position: static; }
</style>
</head>
<body>
<main class="letterhead">
  <header>
    <div class="brand">
      <div class="brand-name">Willow Creek</div>
      <div class="brand-sub">FAMILY MEDICINE</div>
    </div>
    <div class="masthead-right">
      <div class="tagline">HEALING THE WHOLE PERSON</div>
      <div class="doctor">Dr. Martin Hale</div>
    </div>
  </header>

  <div class="rx">R<sub>x</sub></div>

  <div class="watermark-area" role="img" aria-label="Faint brand watermark area"></div>

  <footer class="footer">
    <svg width="740" height="80" viewBox="0 0 740 80" aria-hidden="true">
      <defs>
        <linearGradient id="goldEdge" x1="0" x2="1" y1="0" y2="0">
          <stop offset="0" stop-color="var(--gold-deep)"/>
          <stop offset="0.5" stop-color="var(--gold-light)"/>
          <stop offset="1" stop-color="var(--gold-deep)"/>
        </linearGradient>
      </defs>
      <path d="M0 55 Q370 -35 740 55 L740 80 L0 80 Z" fill="url(#goldEdge)"/>
      <path d="M0 62 Q370 -14 740 62 L740 80 L0 80 Z" fill="var(--band-green)"/>
    </svg>

    <div class="footer-text address">
      <span class="item">
        <svg width="10" height="13" viewBox="0 0 10 13" fill="none" stroke="#fff" stroke-width="1"><path d="M5 12 C2 8 1 6 1 4.5 A4 4 0 0 1 9 4.5 C9 6 8 8 5 12Z"/><circle cx="5" cy="4.5" r="1.4"/></svg>
        #210, ALDER PLAZA, 4B17, USA
      </span>
    </div>

    <div class="footer-text contacts">
      <span class="item">
        <svg width="15" height="10" viewBox="0 0 15 10" fill="none" stroke="#fff" stroke-width="1"><rect x="0.5" y="0.5" width="14" height="9"/><path d="M0.5 0.5 L7.5 6 L14.5 0.5"/></svg>
        willowcreek@mail.com
      </span>
      <span class="item">
        <svg width="17" height="15" viewBox="0 0 17 15" fill="none" stroke="#fff" stroke-width="1"><rect x="4" y="0.5" width="9" height="4"/><rect x="0.5" y="4.5" width="16" height="7"/><rect x="4" y="9" width="9" height="5.5"/></svg>
        01234 555 0190
      </span>
      <span class="item">
        <svg width="10" height="16" viewBox="0 0 10 16" fill="none" stroke="#fff" stroke-width="1"><rect x="0.5" y="0.5" width="9" height="15" rx="1.5"/><line x1="3.5" y1="13" x2="6.5" y2="13"/></svg>
        +01 5550142367
      </span>
      <span class="item">
        <svg width="18" height="12" viewBox="0 0 18 12" fill="none" stroke="#fff" stroke-width="1"><path d="M1 4 Q9 -2 17 4 L15 6 L12 4.5 L12 3 Q9 2 6 3 L6 4.5 L3 6 Z"/><path d="M5 6 L4 11 L14 11 L13 6 Z"/><circle cx="9" cy="8.5" r="1.3"/></svg>
        020 0100 555678
      </span>
      <span class="item">
        <svg width="13" height="13" viewBox="0 0 13 13" fill="none" stroke="#fff" stroke-width="1"><circle cx="6.5" cy="6.5" r="6"/><ellipse cx="6.5" cy="6.5" rx="2.6" ry="6"/><line x1="0.5" y1="6.5" x2="12.5" y2="6.5"/></svg>
        willowcreekclinic.com
      </span>
    </div>
  </footer>
</main>
</body>
</html>
```